Tidemoor Charters website

Looking to have a new, interactive website built on Wordpress and hosted by hostbrivo. Our current site was made and is hosted by plem and has been up and running for 8 years. Would like to replace as seamlessly as possible. Attached are general ideas for the site as well as requirements. Would like to showcase our charter options and information on the home page with Our Charters, FAQ and Gallery as follow up pages. Would like to be created in Wordpress and HTTPS

Target Market(s)

Vacationing tourists visiting Siesta Key

Industry/Entity Type

Boat Charters

Number of Pages Required

1 page

Requirements
Must have
• Website must be secure, HTTPS not HTTP . . Use webp images throughout the entire site. Info for the home page was uploaded on 3 seperate pages labeled home1, home2 and home3. Need the bottom, above footer, to show What Our Customers Say About Us with reviews from Wandermark, Zentra and QP. Homepage to have all 6 charter options and info provided on the attached docx labeled home1, home2 and home3 . If we can get the 3 pages following the home page (Our Charters,FAQ and Gallery) I had also attached brief summaries for those pages. Install these Plug-ins, YOST, Fareharbor (free), Elementor plugin. Any other plugin needs to be approved by us

```html
<!DOCTYPE html>
<html lang="en">
<head>
<meta charset="utf-8">
<title>Tidemoor Charters – Private Boat Tours on Siesta Key</title>
<link href="https://fonts.googleapis.com/css2?family=Outfit:wght@400;500;600;700;800&display=swap" rel="stylesheet">
<style>
:root{
  --orange:#f26522;
  --orange-soft:#f7941d;
  --blue:#0a8ad0;
  --navy:#0b2f55;
  --navy-deep:#0a2444;
  --ink:#111;
  --body:#555;
  --cream:#fdf0ea;
  --white:#fff;
}
*{box-sizing:border-box;margin:0;padding:0}
html,body{width:1200px;height:4071px;overflow:hidden}
body{position:relative;font-family:"Outfit",sans-serif;color:var(--ink);background:var(--white)}
.abs{position:absolute}
svg{display:block}

/* top bar */
.topbar{left:522px;top:0;width:569px;height:41px;background:var(--orange);clip-path:polygon(0 0,100% 0,97% 100%,3% 100%);color:#fff;font-size:14px;display:flex;align-items:center;justify-content:center;gap:18px}
.topbar span{display:flex;align-items:center;gap:8px}
.header{left:0;top:0;width:1200px;height:111px;background:#fff;z-index:2}
.header-fill{left:0;top:41px;width:1200px;height:70px;background:#fff}
.logo{left:107px;top:15px;width:160px;height:160px;border-radius:50%;background:#fff;box-shadow:0 4px 14px rgba(0,0,0,.15);display:flex;align-items:center;justify-content:center;text-align:center;z-index:3;font-weight:700;font-size:20px;line-height:1.1;color:var(--navy)}
.nav{top:66px;left:360px;display:flex;gap:0;z-index:3;font-weight:500;font-size:16px}
.nav a{position:absolute;color:var(--ink);text-decoration:none;white-space:nowrap}
.nav a.active{color:var(--orange)}
.btn{display:flex;align-items:center;justify-content:center;gap:10px;border-radius:30px;color:#fff;font-weight:600;font-size:15px;text-decoration:none}
.btn-navy{background:linear-gradient(90deg,#0a79bd,var(--navy-deep))}
.btn-orange{background:linear-gradient(90deg,var(--orange-soft),var(--orange))}

/* hero */
.hero{left:0;top:111px;width:1200px;height:650px;background:linear-gradient(160deg,#3d5f82 0%,#6f8fb0 35%,#5a7d9a 55%,#2f5874 80%,#1d4763 100%)}
.hero-eyebrow{left:111px;top:240px;color:var(--orange);font-weight:700;font-style:italic;font-size:18px}
.hero-title{left:111px;top:272px;color:#fff;font-weight:800;font-size:63px;line-height:68px;text-transform:uppercase}
.hero-title .lead{font-style:italic}
.hero-text{left:111px;top:490px;width:470px;color:#fff;font-size:16px;line-height:32px}

/* section headings */
.eyebrow{color:var(--orange);font-weight:500;font-size:19px;text-transform:uppercase;text-align:center;width:1200px;left:0}
.title{font-weight:700;font-size:40px;text-transform:uppercase;text-align:center;width:1200px;left:0;line-height:52px}

/* services */
.service{width:222px;text-align:center}
.service .photo{width:222px;height:222px;border-radius:50%;border:6px solid #fff;box-shadow:0 4px 14px rgba(0,0,0,.2)}
.service p{margin-top:22px;font-weight:600;font-size:16px}

/* booking band */
.band{left:0;top:1431px;width:1200px;height:656px;background:linear-gradient(180deg,#0c86c9,#0a6fab)}
.band .eyebrow{color:#fff;font-size:18px}
.band .title{color:#fff;font-size:41px}
.features{left:160px;top:1710px;width:900px;display:flex;justify-content:space-between;color:#fff;font-size:20px}
.features span{display:flex;align-items:center;gap:14px}
.band-photo{left:150px;top:1769px;width:898px;height:471px;border-radius:24px;background:linear-gradient(180deg,#5d6a78 0%,#c98b4c 45%,#f0b24b 58%,#6a5a4d 70%,#2a3a4a 100%);box-shadow:0 10px 30px rgba(0,0,0,.25)}
.custom-text{left:150px;top:2283px;font-size:20px;color:#444}
.custom-link{left:152px;top:2324px;font-size:16px;font-style:italic;color:var(--orange);text-decoration:underline}

/* about */
.about-photo{left:111px;top:2430px;width:488px;height:457px;border-radius:30px;background:linear-gradient(180deg,#7fb0db 0%,#b7d3ea 35%,#4c7fa6 60%,#2f5f80 100%)}
.about-eyebrow{left:677px;top:2470px;color:var(--orange);font-weight:500;font-size:19px}
.about-title{left:677px;top:2496px;font-weight:700;font-size:40px}
.about-text{left:677px;top:2550px;width:420px;font-size:13.5px;line-height:27.5px;color:var(--body)}
.about-bold{left:677px;top:2727px;width:460px;font-size:14px;line-height:28px;color:#222;font-weight:500}

/* reviews */
.reviews{left:0;top:2991px;width:1200px;height:700px;background:var(--cream)}
.card-back{left:169px;top:3241px;width:862px;height:292px;border-radius:24px;background:#fff;opacity:.75;border-bottom:3px solid var(--orange)}
.card{left:226px;top:3214px;width:748px;height:348px;border-radius:24px;background:#fff;box-shadow:0 6px 20px rgba(0,0,0,.06);border-bottom:3px solid var(--orange);text-align:center}
.card .quote{margin:28px auto 0;width:40px}
.card .text{margin:24px auto 0;width:560px;font-size:15.5px;line-height:28.5px;color:#666}
.card .name{margin-top:12px;color:var(--orange);font-size:17px;font-weight:500}
.card .source{margin-top:10px;font-size:22px;font-weight:600;color:var(--blue)}

/* footer */
.footer{left:0;top:3573px;width:1200px;height:498px;background:var(--navy-deep)}
.foot-logo{left:134px;top:3782px;width:174px;height:174px;border-radius:50%;background:#fff;display:flex;align-items:center;justify-content:center;text-align:center;font-weight:700;font-size:21px;line-height:1.1;color:var(--navy)}
.foot-col{color:#fff}
.foot-col h4{font-weight:700;font-size:21px;text-transform:uppercase;margin-bottom:16px}
.foot-col li{list-style:none;display:flex;align-items:flex-start;gap:14px;font-size:15px;line-height:32px}
.foot-col li svg{margin-top:9px;flex:none}
.divider{left:111px;top:4013px;width:978px;height:1px;background:rgba(255,255,255,.25)}
.copyright{left:0;top:4031px;width:1200px;text-align:center;color:#fff;font-size:13px}
</style>
</head>
<body>

<!-- header -->
<div class="abs header-fill" style="z-index:2"></div>
<div class="abs topbar" style="z-index:3">
  <span><svg width="14" height="14" viewBox="0 0 24 24"><rect x="1" y="1" width="22" height="22" rx="4" fill="#fff"/><path d="M8 6l2 0 1 3-1.5 1a8 8 0 0 0 4.5 4.5l1-1.5 3 1v2c0 1-1 2-2 2A12 12 0 0 1 6 8c0-1 1-2 2-2z" fill="var(--orange)"/></svg>Call Us: +1 555-014-2290</span>
  <span>|</span>
  <span><svg width="16" height="12" viewBox="0 0 16 12"><rect width="16" height="12" rx="1.5" fill="#fff"/><path d="M1 1l7 6 7-6" stroke="var(--orange)" stroke-width="1.5" fill="none"/></svg>Email Us: captain@tidemoorcharters.com</span>
</div>
<div class="abs logo">Tidemoor<br>Charters</div>
<nav class="abs nav" style="left:0;top:66px">
  <a class="active" style="left:360px">Home</a>
  <a style="left:444px">About Us</a>
  <a style="left:552px">Our Charters</a>
  <a style="left:690px">FAQ</a>
  <a style="left:761px">Gallery</a>
  <a style="left:855px">Reviews</a>
</nav>
<a class="abs btn btn-navy" style="left:944px;top:58px;width:144px;height:42px;z-index:3">Book Now <svg width="14" height="14" viewBox="0 0 14 14"><circle cx="7" cy="7" r="7" fill="#fff"/><path d="M5.5 4l3 3-3 3" stroke="#0b2f55" stroke-width="1.8" fill="none"/></svg></a>

<!-- hero -->
<div class="abs hero" role="img" aria-label="Dolphin leaping from the water beside a boat's wake near Siesta Key"></div>
<div class="abs hero-eyebrow">UNFORGETTABLE JOURNEYS ON THE WATER</div>
<h1 class="abs hero-title"><span class="lead">Best Private</span><br>Boat Tour on<br>Siesta Key</h1>
<p class="abs hero-text">Dolphin tours, snorkeling, sandbars to tiki bars. Many more options available to make your day perfect!</p>
<a class="abs btn btn-orange" style="left:111px;top:569px;width:144px;height:41px">Book Now <svg width="14" height="14" viewBox="0 0 14 14"><circle cx="7" cy="7" r="7" fill="#fff"/><path d="M5.5 4l3 3-3 3" stroke="#f26522" stroke-width="1.8" fill="none"/></svg></a>
<svg class="abs" style="left:0;top:630px" width="1200" height="135" viewBox="0 0 1200 135">
  <path d="M0 135 L0 130 Q600 -10 1200 130 L1200 135 Z" fill="#fff"/>
  <path d="M105 112 Q600 -20 1095 112 Q600 10 105 112 Z" fill="var(--blue)"/>
</svg>

<!-- services -->
<div class="abs eyebrow" style="top:734px">What We Do</div>
<h2 class="abs title" style="top:762px">Services We Provide</h2>

<div class="abs service" style="left:113px;top:842px"><div class="photo" role="img" aria-label="Dolphin jumping beside the shoreline" style="background:linear-gradient(180deg,#8cb6e0,#3c6e9e 60%,#1f4a72)"></div><p>Dolphin/Wildlife Tours</p></div>
<div class="abs service" style="left:360px;top:842px"><div class="photo" role="img" aria-label="Guests relaxing in shallow water on a sandbar" style="background:linear-gradient(180deg,#bcd6ec,#79c9c9 55%,#3fa9b6)"></div><p>Sandbar Fun</p></div>
<div class="abs service" style="left:608px;top:842px"><div class="photo" role="img" aria-label="Child snorkeling in green water" style="background:radial-gradient(circle at 50% 60%,#3c8a78,#1f5a4d)"></div><p>Snorkeling</p></div>
<div class="abs service" style="left:360px;top:1143px"><div class="photo" role="img" aria-label="Driftwood tree on a white sand beach" style="background:linear-gradient(180deg,#5a91d2,#a8cdea 45%,#6fcbc9 62%,#e9e3d3 75%)"></div><p>Shelling &amp; Beaches</p></div>
<div class="abs service" style="left:608px;top:1143px"><div class="photo" role="img" aria-label="Toddler in a life jacket on a float" style="background:linear-gradient(180deg,#b8cfe3,#8fb9cf 50%,#6aa6b8)"></div><p>Tiki Bar Crawl</p></div>
<div class="abs service" style="left:855px;top:1143px"><div class="photo" role="img" aria-label="Sun setting over calm water" style="background:linear-gradient(180deg,#e7a061,#f2c27b 45%,#6b8a96 62%,#3b6676)"></div><p>Sunset Cruise</p></div>

<!-- booking band -->
<div class="abs band"></div>
<svg class="abs" style="left:0;top:1425px" width="1200" height="125" viewBox="0 0 1200 125">
  <path d="M0 0 L1200 0 L1200 8 Q600 175 0 8 Z" fill="#fff"/>
  <path d="M105 37 Q600 170 1095 37 Q600 135 105 37 Z" fill="var(--orange)"/>
</svg>
<div class="abs eyebrow" style="top:1604px;color:#fff;font-size:18px">Join With Us</div>
<h2 class="abs title" style="top:1637px;color:#fff;font-size:41px">Book Your Siesta Key Boat Charter Today!</h2>
<div class="abs features">
  <span><svg width="17" height="17" viewBox="0 0 18 18"><circle cx="9" cy="9" r="7.5" stroke="#fff" stroke-width="2" fill="none"/><circle cx="9" cy="9" r="3" fill="#fff"/></svg>Dolphin Tours</span>
  <span><svg width="17" height="17" viewBox="0 0 18 18"><circle cx="9" cy="9" r="7.5" stroke="#fff" stroke-width="2" fill="none"/><circle cx="9" cy="9" r="3" fill="#fff"/></svg>Snorkeling</span>
  <span><svg width="17" height="17" viewBox="0 0 18 18"><circle cx="9" cy="9" r="7.5" stroke="#fff" stroke-width="2" fill="none"/><circle cx="9" cy="9" r="3" fill="#fff"/></svg>Sandbars</span>
  <span><svg width="17" height="17" viewBox="0 0 18 18"><circle cx="9" cy="9" r="7.5" stroke="#fff" stroke-width="2" fill="none"/><circle cx="9" cy="9" r="3" fill="#fff"/></svg>Tiki Bars</span>
  <span><svg width="17" height="17" viewBox="0 0 18 18"><circle cx="9" cy="9" r="7.5" stroke="#fff" stroke-width="2" fill="none"/><circle cx="9" cy="9" r="3" fill="#fff"/></svg>Shelling</span>
  <span><svg width="17" height="17" viewBox="0 0 18 18"><circle cx="9" cy="9" r="7.5" stroke="#fff" stroke-width="2" fill="none"/><circle cx="9" cy="9" r="3" fill="#fff"/></svg>Sunsets</span>
</div>
<div class="abs band-photo" role="img" aria-label="Catamaran sailing at sunset on the Gulf"></div>
<p class="abs custom-text">Design your day on the water. Customize your day your way!</p>
<a class="abs custom-link">Call or Email to coordinate and get help with suggestions.</a>
<a class="abs btn btn-navy" style="left:904px;top:2288px;width:144px;height:42px">Book Now <svg width="14" height="14" viewBox="0 0 14 14"><circle cx="7" cy="7" r="7" fill="#fff"/><path d="M5.5 4l3 3-3 3" stroke="#0b2f55" stroke-width="1.8" fill="none"/></svg></a>

<!-- about -->
<div class="abs about-photo" role="img" aria-label="Charter deck boat with guests under a canopy"></div>
<div class="abs about-eyebrow">ABOUT</div>
<h2 class="abs about-title">WHO WE ARE</h2>
<p class="abs about-text">Welcome to the BEST private charter on and around Siesta Key! Whether you live on Siesta Key, Sarasota or are one of our many welcome visitors... we want you to enjoy the day on the crystal clear waters and pristine beaches. My name is Sam Rowe and I look forward to being your Captain for the day. My goal is to ensure a safe and fun time on the water.</p>
<p class="abs about-bold">I will work hard to create unforgettable memories<br>with a charter that you, your family and friends will remember.</p>
<a class="abs btn btn-navy" style="left:677px;top:2798px;width:145px;height:43px">Read More <svg width="14" height="14" viewBox="0 0 14 14"><circle cx="7" cy="7" r="7" fill="#fff"/><path d="M5.5 4l3 3-3 3" stroke="#0b2f55" stroke-width="1.8" fill="none"/></svg></a>

<!-- reviews -->
<div class="abs reviews"></div>
<div class="abs eyebrow" style="top:3049px">Reviews</div>
<h2 class="abs title" style="top:3082px">What Our Charter Guests Have To<br>Say About Us</h2>
<div class="abs card-back"></div>
<div class="abs card">
  <svg class="quote" width="40" height="32" viewBox="0 0 40 32"><path d="M2 0h15v16c0 9-5 15-13 16l-1-5c4-1 6-4 6-8H2z M23 0h15v16c0 9-5 15-13 16l-1-5c4-1 6-4 6-8h-7z" fill="var(--orange)"/></svg>
  <p class="text">Sed ut perspiciatis unde omnis iste natus error sit voluptatem accusantium doloremque laudantium, totam rem aperiam, eaque ipsa quae ab illo inventore veritatis et quasi architecto beatae vitae dicta sunt explicabo. Nemo enim ipsam voluptatem quia voluptas sit aspernatur</p>
  <p class="name">Jordan Pell, United States</p>
  <p class="source">Zentra</p>
</div>

<!-- footer -->
<div class="abs footer"></div>
<svg class="abs" style="left:0;top:3565px" width="1200" height="130" viewBox="0 0 1200 130">
  <path d="M0 0 L1200 0 L1200 8 Q600 170 0 8 Z" fill="var(--cream)"/>
  <path d="M105 42 Q600 165 1095 42 Q600 130 105 42 Z" fill="var(--blue)"/>
</svg>
<div class="abs foot-logo">Tidemoor<br>Charters</div>

<div class="abs foot-col" style="left:390px;top:3775px">
  <h4>Quick Links</h4>
  <ul>
    <li><svg width="14" height="14" viewBox="0 0 14 14"><circle cx="7" cy="7" r="7" fill="#fff"/><path d="M5.5 4l3 3-3 3" stroke="#0a2444" stroke-width="1.8" fill="none"/></svg>About Us</li>
    <li><svg width="14" height="14" viewBox="0 0 14 14"><circle cx="7" cy="7" r="7" fill="#fff"/><path d="M5.5 4l3 3-3 3" stroke="#0a2444" stroke-width="1.8" fill="none"/></svg>Our Charters</li>
    <li><svg width="14" height="14" viewBox="0 0 14 14"><circle cx="7" cy="7" r="7" fill="#fff"/><path d="M5.5 4l3 3-3 3" stroke="#0a2444" stroke-width="1.8" fill="none"/></svg>FAQ</li>
    <li><svg width="14" height="14" viewBox="0 0 14 14"><circle cx="7" cy="7" r="7" fill="#fff"/><path d="M5.5 4l3 3-3 3" stroke="#0a2444" stroke-width="1.8" fill="none"/></svg>Gallery</li>
    <li><svg width="14" height="14" viewBox="0 0 14 14"><circle cx="7" cy="7" r="7" fill="#fff"/><path d="M5.5 4l3 3-3 3" stroke="#0a2444" stroke-width="1.8" fill="none"/></svg>Reviews</li>
  </ul>
</div>

<div class="abs foot-col" style="left:604px;top:3775px;width:300px">
  <h4>Contact Us</h4>
  <ul>
    <li><svg width="12" height="15" viewBox="0 0 12 16"><path d="M6 0a6 6 0 0 1 6 6c0 4-6 10-6 10S0 10 0 6a6 6 0 0 1 6-6z" fill="#fff"/><circle cx="6" cy="6" r="2.2" fill="#0a2444"/></svg>Departs from 4120 Gull Harbor Rd,<br>Siesta Key, FL, United States,<br>Florida.</li>
    <li><svg width="14" height="14" viewBox="0 0 24 24"><path d="M5 2l4 0 2 5-2.5 1.5a11 11 0 0 0 7 7L17 13l5 2v4c0 1.5-1.5 3-3 3A17 17 0 0 1 2 5c0-1.5 1.5-3 3-3z" fill="#fff"/></svg>+1 555-014-2290</li>
    <li><svg width="15" height="12" viewBox="0 0 16 12"><rect width="16" height="12" rx="1.5" fill="#fff"/><path d="M1 1l7 6 7-6" stroke="#0a2444" stroke-width="1.5" fill="none"/></svg>captain@tidemoorcharters.com</li>
  </ul>
</div>

<div class="abs foot-col" style="left:938px;top:3775px">
  <h4>Follow Us</h4>
  <ul>
    <li><svg width="14" height="14" viewBox="0 0 14 14"><circle cx="7" cy="7" r="7" fill="#fff"/><path d="M5.5 4l3 3-3 3" stroke="#0a2444" stroke-width="1.8" fill="none"/></svg>Friendwall</li>
    <li><svg width="14" height="14" viewBox="0 0 14 14"><circle cx="7" cy="7" r="7" fill="#fff"/><path d="M5.5 4l3 3-3 3" stroke="#0a2444" stroke-width="1.8" fill="none"/></svg>Chirpline</li>
    <li><svg width="14" height="14" viewBox="0 0 14 14"><circle cx="7" cy="7" r="7" fill="#fff"/><path d="M5.5 4l3 3-3 3" stroke="#0a2444" stroke-width="1.8" fill="none"/></svg>Snapgrid</li>
    <li><svg width="14" height="14" viewBox="0 0 14 14"><circle cx="7" cy="7" r="7" fill="#fff"/><path d="M5.5 4l3 3-3 3" stroke="#0a2444" stroke-width="1.8" fill="none"/></svg>Viewtube</li>
  </ul>
</div>

<div class="abs divider"></div>
<p class="abs copyright">(C) Copyright 2024 | All Rights Reserved</p>

</body>
</html>
```